Menu Design Project

Bel Roux hair and beauty service menu
we need a menu to display a handful of our services to give our customers an idea of our pricing

Cutting
Ladies cuts from $35
Men's cuts from $25
All cuts are included with a wash and dry off

Velora colours
All over colours start from $55
price will vary depending upon length and thickness of hair

Foiling
starts from $50
Price will vary depending upon length of hair

Toners
from $30

Blowdries
from $35

Upstyling
wedding styling from $45
Please enquire for special occasion styling also

Beauty Services

Waxing
Eyebrow wax and shape $17.50
Lip $10
Chin/sides $20
Legs from $25
Bikini $20
XX $30
XXX $45
Back from $25
Chest from $25

Eyes
Eyebrow tinting $15
Eyelash tinting $20
Eyelash extensions from $90

Derminia facials
Express facial $45
Deluxe facial $95

Acrylic nails
full set $60
Gel polish $35
Manicures from $35
Pedicures from $45

can provide logo and other images to help

Industry/Entity Type

Hair

Requirements
Must have
• must be called a service menu
must be eye catching and memorable but not excessive
Nice to have
• postcard style size hair menu on one side
beauty menu on the other side
elegant classy design
Should not have
• must not be called a price list
stay away from traditional price list style in terms of folding out leaflet

```html
<!DOCTYPE html>
<html lang="en">
<head>
<meta charset="utf-8">
<title>Bel Roux Hair and Beauty Service Menu</title>
<link rel="stylesheet" href="https://fonts.googleapis.com/css2?family=Righteous&family=Fira+Sans:wght@400;600&display=swap">
<style>
  :root {
    --backdrop: #7a0f36;
    --card-teal: #0e9e9a;
    --ink-white: #ffffff;
    --hair-copper: #d65a2e;
    --rose-berry: #a83050;
    --polish-plum: #7d3a63;
    --polish-nude: #d8c0b2;
    --skin-warm: #d9b39a;
  }
  * { box-sizing: border-box; margin: 0; padding: 0; }
  html, body { width: 1200px; height: 800px; overflow: hidden; }
  body {
    background: var(--backdrop);
    position: relative;
    font-family: "Fira Sans", sans-serif;
    color: var(--ink-white);
  }
  .menu-card {
    position: absolute;
    top: 110px;
    width: 420px;
    height: 580px;
    background: var(--card-teal);
    box-shadow: 0 10px 28px rgba(0,0,0,0.35);
    overflow: hidden;
  }
  .menu-card--hair { left: 150px; }
  .menu-card--beauty { left: 630px; }
  .card-art {
    position: absolute;
    inset: 0;
    width: 420px;
    height: 580px;
  }
  .menu-title {
    position: absolute;
    left: 56px;
    top: 32px;
    font-family: "Righteous", sans-serif;
    font-weight: 400;
    font-size: 16px;
    line-height: 1.25;
    letter-spacing: 0.2px;
  }
  .service-list {
    position: absolute;
    left: 64px;
    top: 100px;
    width: 320px;
    font-size: 12.5px;
    line-height: 1.2;
  }
  .service-group { margin-bottom: 16px; }
  .menu-card--beauty .service-list { width: 200px; top: 100px; }
  .menu-card--beauty .service-group { margin-bottom: 20px; }
  .service-name { font-weight: 600; }
  .service-line { font-weight: 400; }
</style>
</head>
<body>

<section class="menu-card menu-card--hair" aria-label="Hair service menu">
  <svg class="card-art" viewBox="0 0 420 580">
    <g class="frame-lines" fill="var(--ink-white)">
      <rect x="12" y="0" width="4" height="580"/>
      <rect x="24" y="0" width="4" height="580"/>
      <rect x="0" y="532" width="420" height="4"/>
      <rect x="0" y="544" width="420" height="4"/>
    </g>
    <defs>
      <radialGradient id="hairTone" cx="40%" cy="40%" r="70%">
        <stop offset="0" stop-color="#e8744a"/>
        <stop offset="1" stop-color="var(--hair-copper)"/>
      </radialGradient>
    </defs>
    <circle cx="314" cy="56" r="30" fill="var(--rose-berry)" stroke="var(--ink-white)" stroke-width="3" role="img" aria-label="Photo of rolled red and purple ribbon roses"/>
    <circle cx="372" cy="66" r="46" fill="url(#hairTone)" stroke="var(--ink-white)" stroke-width="3" role="img" aria-label="Close-up photo of copper red hair"/>
    <g class="accent-dots" fill="var(--ink-white)">
      <circle cx="296" cy="18" r="6"/>
      <circle cx="338" cy="98" r="6"/>
      <circle cx="406" cy="96" r="8"/>
    </g>
  </svg>
  <h1 class="menu-title">Bel Roux Hair and Beauty<br>Service Menu</h1>
  <div class="service-list">
    <div class="service-group">
      <p class="service-name">Cutting</p>
      <p class="service-line">Ladies cuts from $35</p>
      <p class="service-line">Men's cuts from $25</p>
      <p class="service-line">All cuts are included with a wash and dry off</p>
    </div>
    <div class="service-group">
      <p class="service-name">Velora colours</p>
      <p class="service-line">All over colours start from $55</p>
      <p class="service-line">Price will vary depending upon length and thickness of hair</p>
    </div>
    <div class="service-group">
      <p class="service-name">Foiling</p>
      <p class="service-line">Starts from $50</p>
      <p class="service-line">Price will vary depending upon length of hair</p>
    </div>
    <div class="service-group">
      <p class="service-name">Toners</p>
      <p class="service-line">From $30</p>
    </div>
    <div class="service-group">
      <p class="service-name">Blowdries</p>
      <p class="service-line">From $35</p>
      <p class="service-line">Price will vary depending upon length and thickness of hair</p>
    </div>
    <div class="service-group">
      <p class="service-name">Upstyling</p>
      <p class="service-line">Wedding styling from $45</p>
      <p class="service-line">Please also enquire for special occasion styling</p>
    </div>
  </div>
</section>

<section class="menu-card menu-card--beauty" aria-label="Beauty service menu">
  <svg class="card-art" viewBox="0 0 420 580">
    <g class="frame-lines" fill="var(--ink-white)">
      <rect x="12" y="0" width="4" height="580"/>
      <rect x="24" y="0" width="4" height="580"/>
      <rect x="0" y="532" width="420" height="4"/>
      <rect x="0" y="544" width="420" height="4"/>
    </g>
    <defs>
      <linearGradient id="polishTone" x1="0" y1="0" x2="1" y2="0">
        <stop offset="0" stop-color="var(--polish-nude)"/>
        <stop offset="0.55" stop-color="var(--polish-plum)"/>
        <stop offset="1" stop-color="#9a3d6a"/>
      </linearGradient>
    </defs>
    <circle cx="335" cy="130" r="75" fill="url(#polishTone)" stroke="var(--ink-white)" stroke-width="3" role="img" aria-label="Photo of three nail polish bottles in nude and plum shades"/>
    <circle cx="262" cy="205" r="48" fill="var(--skin-warm)" stroke="var(--ink-white)" stroke-width="3" role="img" aria-label="Close-up photo of an eye with defined lashes"/>
    <g class="accent-dots" fill="var(--ink-white)">
      <circle cx="385" cy="52" r="12"/>
      <circle cx="240" cy="150" r="7"/>
      <circle cx="318" cy="278" r="18"/>
    </g>
  </svg>
  <h1 class="menu-title">Bel Roux Hair and Beauty<br>Service Menu</h1>
  <div class="service-list">
    <div class="service-group">
      <p class="service-name">Waxing</p>
      <p class="service-line">Eyebrow wax and shape $17.50</p>
      <p class="service-line">Lip $10</p>
      <p class="service-line">Chin/sides $20</p>
      <p class="service-line">Legs from $25</p>
      <p class="service-line">Bikini $20</p>
      <p class="service-line">XX $30</p>
      <p class="service-line">XXX $45</p>
      <p class="service-line">Back from $25</p>
      <p class="service-line">Chest from $25</p>
    </div>
    <div class="service-group">
      <p class="service-name">Eyes</p>
      <p class="service-line">Eyebrow tinting $15</p>
      <p class="service-line">Eyelash tinting $20</p>
      <p class="service-line">Eyelash extensions from $90</p>
    </div>
    <div class="service-group">
      <p class="service-name">Derminia facials</p>
      <p class="service-line">Express facial $45</p>
      <p class="service-line">Deluxe facial $95</p>
    </div>
    <div class="service-group">
      <p class="service-name">Acrylic nails</p>
      <p class="service-line">Full set $60</p>
      <p class="service-line">Gel polish $35</p>
      <p class="service-line">Manicures from $35</p>
      <p class="service-line">Pedicures from $45</p>
    </div>
  </div>
</section>

</body>
</html>
```